Animal Feed Bag Packaging Design

The task is to design a livestock feed bag. These are 18"x32" and typically hold 50 LBS of feed. This design will be on all of the packaging for our feed bags. These feed bags will be sold in local feed and hardware stores and will hold a variety of different feed products for all classes of livestock. The bags will be double sided. I would like the back side to remain consistent, but I would like the front of the bag to have 4 different varieties that share the same layout, but incorporate different titles and possible graphics. The Categories will be:
- "Poultry Feed" This will be for all classes of poultry
- "Hog Feed" This will be for all classes of hogs
- "Mixed Feed" This will be a sort of catch all design that will be used for a variety of different types of livestock feed (cows, goats, sheep, rabbits)
- "Feed & Grain": This will also be a miscelaneous category that will be used for whole grains and feeds that can be used across multiple animal types.

I have attached many photos that may or may not be used, but that may help to portray our operation and what we do.

Target Market(s)

Backyard Hobby Farmers and Livestock Enthusists

Industry/Entity Type

Agriculture

Font styles to use
Serif

Colors

Designer to choose colors to be used in the design.

Requirements
Must have
• Must contain our logo and have a strong brand presence for "Calloway Kin's Feed". Each bag needs to contain the the following on either the front or backside of the bag. Calloway Kin's Feed - 214 North Willow Lane Brackmoor Utah, 61392 - 608 271 5519 - callowaykinsfeed.example
Nice to have
• Our brand is built around these factors that could be incorporated into the design: Locally Milled, Quality Ingredients, Balanced Nutrition, Family Owned & Operated Est. 2017. Home delivery is also a core competency of our operation. I will attach a few images of our farm where we operate at that may be incorporated if it fits the style.

```html
<!DOCTYPE html>
<html lang="en">
<head>
<meta charset="utf-8">
<title>Calloway Kin's Feed – Poultry Feed Bag</title>
<link href="https://fonts.googleapis.com/css2?family=Archivo:wdth,wght@100..125,700..900&family=Montserrat:wght@500;600;700&display=swap" rel="stylesheet">
<style>
  :root {
    --teal: #13918a;
    --teal-text: #0f8d83;
    --yellow: #f9be34;
    --white: #ffffff;
    --backdrop: #ececec;
    --sky-top: #3f97de;
    --sky-low: #a9d0ee;
    --grass: #5f922f;
    --soil: #7b6a43;
    --field: #4f8a2e;
    --field-dark: #355f22;
  }
  * { box-sizing: border-box; margin: 0; padding: 0; }
  html, body { width: 1200px; height: 2260px; overflow: hidden; }
  body {
    background: var(--backdrop);
    font-family: "Montserrat", Arial, sans-serif;
    position: relative;
  }
  .bag-side {
    position: absolute;
    top: 632px;
    width: 560px;
    height: 995px;
    background: var(--white);
    overflow: hidden;
    box-shadow: 0 6px 18px rgba(0,0,0,0.18);
  }
  .bag-front { left: 25px; }
  .bag-back { left: 615px; }
  .layer { position: absolute; left: 0; top: 0; width: 560px; height: 995px; }

  .brand-badge {
    position: absolute;
    left: 179px; top: 58px;
    width: 202px; height: 202px;
    border-radius: 50%;
    background: var(--teal);
    display: flex; align-items: center; justify-content: center;
    text-align: center;
  }
  .brand-name {
    color: var(--white);
    font-family: "Archivo", Arial, sans-serif;
    font-weight: 800;
    font-stretch: 112%;
    font-size: 17px;
    letter-spacing: 0.06em;
    text-transform: uppercase;
    line-height: 1.2;
  }

  .title-panel {
    position: absolute;
    left: 48px; top: 563px;
    width: 465px; height: 271px;
    background: var(--teal);
    color: var(--white);
    text-align: center;
    font-family: "Archivo", Arial, sans-serif;
    padding-top: 20px;
  }
  .est-line {
    display: flex; align-items: center; justify-content: center; gap: 10px;
    font-weight: 800; font-stretch: 120%; font-size: 20px; letter-spacing: 0.22em;
    padding: 0 34px;
  }
  .est-line::before, .est-line::after {
    content: ""; flex: 1; height: 2px; background: var(--white);
  }
  .feed-title {
    font-weight: 900; font-stretch: 125%;
    font-size: 68px; line-height: 0.98; letter-spacing: -0.01em;
    margin-top: 8px;
  }
  .feed-class {
    color: var(--yellow);
    font-weight: 900; font-stretch: 118%;
    font-size: 29px; line-height: 1.08;
    margin-top: 14px;
  }

  .claims-row {
    position: absolute;
    left: 0; top: 852px; width: 560px;
  }
  .claims {
    position: absolute; top: 8px;
    list-style: none;
    color: var(--teal-text);
    font-weight: 600; font-size: 15px; line-height: 1.08;
    text-transform: uppercase;
  }
  .claims-left { left: 60px; }
  .claims-right { left: 360px; }
  .claims li { position: relative; padding-left: 26px; margin-bottom: 12px; }
  .claims li svg { position: absolute; left: 0; top: 1px; }
  .weight {
    position: absolute; left: 200px; top: -14px; width: 150px;
    text-align: center; color: var(--teal-text);
    font-family: "Archivo", Arial, sans-serif; font-weight: 900; font-stretch: 125%;
  }
  .weight-number { font-size: 118px; line-height: 0.9; letter-spacing: -0.03em; display: block; }
  .weight-unit { font-size: 32px; line-height: 1; display: block; margin-left: 40px; margin-top: -4px; }

  .farm-snapshot {
    position: absolute; top: 575px;
    width: 164px; height: 164px; border-radius: 50%;
    border: 8px solid var(--white);
  }
  .snap-truck { left: 25px; background: linear-gradient(180deg, #9dc0d8 0%, #7c8b5a 45%, #c7b08a 100%); }
  .snap-yard { left: 198px; background: linear-gradient(180deg, #4b7c31 0%, #9a9a88 55%, #5f7d3a 100%); }
  .snap-flock { left: 371px; background: linear-gradient(180deg, #d6c49a 0%, #8a6a3c 55%, #3a2a1e 100%); }

  .back-message {
    position: absolute; left: 0; top: 780px; width: 560px;
    text-align: center; color: var(--teal-text);
    font-family: "Archivo", Arial, sans-serif; font-weight: 900; font-stretch: 115%;
    font-size: 25px; line-height: 1.15; text-transform: uppercase;
  }
  .contact {
    position: absolute; top: 890px;
    list-style: none; color: var(--teal-text);
    font-weight: 600; font-size: 13.5px; line-height: 1.15;
    text-transform: uppercase;
  }
  .contact-left { left: 60px; }
  .contact-right { left: 292px; }
  .contact li { position: relative; padding-left: 28px; margin-bottom: 8px; }
  .contact li svg { position: absolute; left: 0; top: 0; }
</style>
</head>
<body>

  <!-- FRONT -->
  <section class="bag-side bag-front">
    <svg class="layer" viewBox="0 0 560 995" role="img" aria-label="Photograph of a brown hen standing in green grass under a blue sky">
      <defs>
        <linearGradient id="front-photo" x1="0" y1="0" x2="0" y2="1">
          <stop offset="0" stop-color="var(--sky-top)"/>
          <stop offset="0.45" stop-color="var(--sky-low)"/>
          <stop offset="0.62" stop-color="var(--grass)"/>
          <stop offset="1" stop-color="var(--soil)"/>
        </linearGradient>
      </defs>
      <path d="M0,198 Q280,158 560,198 L560,612 Q280,652 0,612 Z" fill="url(#front-photo)"/>
    </svg>
    <svg class="layer" viewBox="0 0 560 995" aria-hidden="true">
      <path d="M0,132 Q280,92 560,132 L560,152 Q280,112 0,152 Z" fill="var(--yellow)"/>
      <path d="M0,152 Q280,112 560,152 L560,198 Q280,158 0,198 Z" fill="var(--teal)"/>
      <path d="M0,612 Q280,652 560,612 L560,638 Q280,678 0,638 Z" fill="var(--teal)"/>
      <path d="M0,638 Q280,678 560,638 L560,658 Q280,698 0,658 Z" fill="var(--yellow)"/>
    </svg>

    <div class="brand-badge"><span class="brand-name">Calloway Kin's Feed</span></div>

    <div class="title-panel">
      <div class="est-line">EST. 2017</div>
      <h1 class="feed-title">POULTRY<br>FEED</h1>
      <p class="feed-class">FOR ALL CLASSES<br>OF POULTRY</p>
    </div>

    <div class="claims-row">
      <ul class="claims claims-left">
        <li><svg width="16" height="16" viewBox="0 0 16 16"><circle cx="8" cy="8" r="8" fill="var(--yellow)"/><path d="M4.5 8.2 L7 10.5 L11.5 5.8" stroke="#fff" stroke-width="2" fill="none"/></svg>Locally<br>Milled</li>
        <li><svg width="16" height="16" viewBox="0 0 16 16"><circle cx="8" cy="8" r="8" fill="var(--yellow)"/><path d="M4.5 8.2 L7 10.5 L11.5 5.8" stroke="#fff" stroke-width="2" fill="none"/></svg>Quality<br>Ingredients</li>
      </ul>
      <div class="weight"><span class="weight-number">50</span><span class="weight-unit">LBS</span></div>
      <ul class="claims claims-right">
        <li><svg width="16" height="16" viewBox="0 0 16 16"><circle cx="8" cy="8" r="8" fill="var(--yellow)"/><path d="M4.5 8.2 L7 10.5 L11.5 5.8" stroke="#fff" stroke-width="2" fill="none"/></svg>Balanced<br>Nutrition</li>
        <li><svg width="16" height="16" viewBox="0 0 16 16"><circle cx="8" cy="8" r="8" fill="var(--yellow)"/><path d="M4.5 8.2 L7 10.5 L11.5 5.8" stroke="#fff" stroke-width="2" fill="none"/></svg>Family Owned<br>&amp; Operated</li>
      </ul>
    </div>
  </section>

  <!-- BACK -->
  <section class="bag-side bag-back">
    <svg class="layer" viewBox="0 0 560 995" role="img" aria-label="Aerial photograph of the family farm with green fields, trees and barns">
      <defs>
        <linearGradient id="back-photo" x1="0" y1="0" x2="1" y2="1">
          <stop offset="0" stop-color="#8a9a5a"/>
          <stop offset="0.4" stop-color="var(--field)"/>
          <stop offset="1" stop-color="var(--field-dark)"/>
        </linearGradient>
      </defs>
      <path d="M0,198 Q280,158 560,198 L560,640 Q280,690 0,640 Z" fill="url(#back-photo)"/>
    </svg>
    <svg class="layer" viewBox="0 0 560 995" aria-hidden="true">
      <path d="M0,132 Q280,92 560,132 L560,152 Q280,112 0,152 Z" fill="var(--yellow)"/>
      <path d="M0,152 Q280,112 560,152 L560,198 Q280,158 0,198 Z" fill="var(--teal)"/>
      <path d="M0,640 Q280,690 560,640 L560,664 Q280,714 0,664 Z" fill="var(--teal)"/>
      <path d="M0,664 Q280,714 560,664 L560,682 Q280,732 0,682 Z" fill="var(--yellow)"/>
    </svg>

    <div class="brand-badge"><span class="brand-name">Calloway Kin's Feed</span></div>

    <div class="farm-snapshot snap-truck" role="img" aria-label="Photograph of a red feed delivery truck in the farmyard"></div>
    <div class="farm-snapshot snap-yard" role="img" aria-label="Photograph of the farm buildings and livestock pens"></div>
    <div class="farm-snapshot snap-flock" role="img" aria-label="Photograph of two roosters standing in the yard"></div>

    <h2 class="back-message">Big or small<br>let us help your livestock<br>operation grow</h2>

    <ul class="contact contact-left">
      <li><svg width="16" height="16" viewBox="0 0 16 16"><circle cx="8" cy="8" r="8" fill="var(--yellow)"/><path d="M8 3.5 a2.8 2.8 0 0 1 2.8 2.8 c0 2 -2.8 5.2 -2.8 5.2 s-2.8 -3.2 -2.8 -5.2 A2.8 2.8 0 0 1 8 3.5 Z" fill="#fff"/><circle cx="8" cy="6.3" r="1" fill="var(--yellow)"/></svg>Calloway Kin's Feed<br>214 North Willow Lane<br>Brackmoor Utah, 61392</li>
    </ul>
    <ul class="contact contact-right">
      <li><svg width="16" height="16" viewBox="0 0 16 16"><circle cx="8" cy="8" r="8" fill="var(--yellow)"/><path d="M5.3 4 L6.8 4 L7.4 6 L6.4 6.8 C7 8 8 9 9.2 9.6 L10 8.6 L12 9.2 L12 10.7 C12 11.2 11.6 11.6 11.1 11.6 C7.6 11.4 4.6 8.4 4.4 4.9 C4.4 4.4 4.8 4 5.3 4 Z" fill="#fff"/></svg>608 271 5519</li>
      <li><svg width="16" height="16" viewBox="0 0 16 16"><circle cx="8" cy="8" r="8" fill="var(--yellow)"/><circle cx="8" cy="8" r="4.2" fill="none" stroke="#fff" stroke-width="1.2"/><path d="M3.8 8 H12.2 M8 3.8 C6 6 6 10 8 12.2 M8 3.8 C10 6 10 10 8 12.2" stroke="#fff" stroke-width="1" fill="none"/></svg>callowaykinsfeed.example</li>
    </ul>
  </section>

</body>
</html>
```